Personal Training Business at home (Brook Vitality & Health)

My business name will be Brook Vitality & Health and will be training people with special needs (Asthma, Diabetes, Obesity, Rehab, Sports Performance) for all ages. It will be set indoor and outdoor for all types of weather conditions. I,m also doing Pilates group classes as well in a Japanese garden setting.I will be working alone so the groups will be small and the client has a high quality of service. I just need something very basic to start with then as the business expands I can edit it to it,s growth.

Target Market(s)

Target special population persons with dysfunctions injuries, metabolic/cardio-respiratory conditions, sports performance and more also healthy food choices.

Industry/Entity Type

Business

Number of Pages Required

3 page

Font styles to use
Serif

Colors
f78f20
ffffff
474747
cbcbcb
abd036

Requirements
Must have
• The website must have accessibility for change, to be able to link on other networks like my own ClipHarbor videos. A basic lay out so I can fill in the pages and ad more as I expand the business. The logo to have the A for Brook to be an image of a man shaped as the letter A with his arms extended out/up. Private Facility and must ring for appointment to enter premises.
Nice to have
• The Image I want to have in my studio is for people to be serious about training & health choices. I want them to be able to train in a comfortable environment and free of air conditioned concrete rooms with machines. My home is converted to a Organic feature and outdoor/indoor training facility that my clients & I can share the natural freedom of training in the elements. My client have special needs and need extra care, they are people with injuries, metabolic/cardio-respiratory condition, asthmatics & more they need to be screened and tested for the condition that they suffer from and together with there allied professional we work together to treat them with the up most care for maximum results. This is what I want to target I long term client with real Goals on there mind and not some pipe dream.
Should not have
• Not to be portray as a Gym with machines and clients that only care about image.

```html
<!DOCTYPE html>
<html lang="en">
<head>
<meta charset="utf-8">
<title>Brook Vitality &amp; Health</title>
<link href="https://fonts.googleapis.com/css2?family=Lora:wght@400;500;600;700&display=swap" rel="stylesheet">
<style>
  :root {
    --ink: #474747;
    --text: #474747;
    --muted: #7a7a7a;
    --faint: #a9a9a9;
    --rule: #cbcbcb;
    --accent: #f78f20;
    --leaf: #abd036;
    --panel: #f4f4f4;
    --white: #ffffff;
  }
  * { box-sizing: border-box; margin: 0; padding: 0; }
  html, body { width: 1010px; height: 1200px; overflow: hidden; background: var(--white); }
  body { position: relative; font-family: "Lora", Georgia, serif; color: var(--text); }

  .site-nav { position: absolute; top: 0; left: 0; width: 1010px; height: 36px; }
  .site-nav__links { position: absolute; left: 134px; top: 11px; display: flex; gap: 20px; list-style: none; font-size: 11px; color: var(--muted); letter-spacing: .2px; }
  .site-nav__links .is-current { color: var(--ink); font-weight: 600; }
  .region { position: absolute; left: 684px; top: 9px; display: flex; gap: 8px; align-items: flex-start; }
  .region__label { font-size: 7.5px; font-weight: 700; color: var(--ink); line-height: 1.3; }
  .region__value { font-size: 7px; color: var(--muted); display: flex; gap: 3px; align-items: center; }
  .login { position: absolute; left: 771px; top: 13px; font-size: 9.5px; color: var(--ink); letter-spacing: .3px; }
  .join-button { position: absolute; left: 808px; top: 8px; width: 69px; height: 20px; border: 1px solid var(--accent); border-radius: 3px; font-size: 8.5px; font-weight: 600; color: var(--accent); display: flex; align-items: center; justify-content: center; }

  .hero { position: absolute; top: 36px; left: 0; width: 1010px; height: 280px; background: linear-gradient(180deg, #c9e27a 0%, var(--leaf) 40%, #5f8a2a 100%); }
  .hero__mark { position: absolute; left: 485px; top: 114px; width: 40px; height: 40px; border: 2px solid var(--white); border-radius: 50%; }
  .hero__name { position: absolute; left: 0; width: 1010px; top: 164px; text-align: center; font-size: 21px; font-weight: 400; letter-spacing: 3.5px; color: var(--white); }
  .hero__tagline { position: absolute; left: 0; width: 1010px; top: 210px; text-align: center; font-size: 20px; font-weight: 700; color: var(--white); word-spacing: 6px; }

  .intro { position: absolute; top: 316px; left: 0; width: 1010px; height: 175px; }
  .intro__col { position: absolute; top: 0; height: 175px; width: 505px; }
  .intro__col--training { left: 0; }
  .intro__col--philosophy { left: 505px; background: var(--panel); }
  .intro__title { position: absolute; top: 34px; left: 0; width: 100%; font-size: 22px; font-weight: 400; color: var(--ink); letter-spacing: .3px; }
  .intro__col--training .intro__title { text-align: center; padding-left: 64px; }
  .intro__col--philosophy .intro__title { left: 87px; }
  .intro__text { position: absolute; top: 86px; width: 300px; font-size: 11px; line-height: 12.5px; color: var(--text); }
  .intro__col--training .intro__text { left: 135px; }
  .intro__col--philosophy .intro__text { left: 48px; }

  .benefits-title { position: absolute; top: 550px; left: 365px; display: flex; align-items: center; gap: 17px; }
  .benefits-title__dot { width: 42px; height: 42px; border: 2px solid var(--leaf); border-radius: 50%; }
  .benefits-title h2 { font-size: 29px; font-weight: 400; color: var(--ink); }

  .benefit { position: absolute; left: 134px; width: 742px; }
  .benefit__photo { position: absolute; left: 0; top: 0; width: 132px; height: 132px; border-radius: 50%; }
  .benefit__body { position: absolute; left: 164px; width: 580px; }
  .benefit__heading { font-size: 14.5px; font-weight: 700; color: var(--accent); letter-spacing: .2px; margin-bottom: 3px; }
  .benefit__text { font-size: 12px; line-height: 16.4px; color: var(--text); }

  .photo-care { background: radial-gradient(circle at 45% 40%, #e4efc6 0%, #9fbf5a 50%, #55702a 100%); }
  .photo-outdoor { background: radial-gradient(circle at 60% 45%, #d9e6b8 0%, #8aa65a 50%, #4a5e33 100%); }
  .photo-pilates { background: radial-gradient(circle at 50% 50%, #fbc98a 0%, var(--accent) 55%, #9a5516 100%); }

  .site-footer { position: absolute; top: 1168px; left: 0; width: 1010px; height: 32px; border-top: 2px solid var(--rule); }
  .site-footer__links { position: absolute; left: 134px; top: 10px; display: flex; gap: 18px; list-style: none; font-size: 9.5px; color: var(--faint); }
  .site-footer__help { position: absolute; left: 688px; top: 10px; font-size: 9.5px; color: var(--faint); }
</style>
</head>
<body>
  <header class="site-nav">
    <ul class="site-nav__links">
      <li class="is-current">HOME PAGE</li>
      <li>MY STORY</li>
      <li>SESSIONS AND PRICING</li>
      <li>COMMUNITY</li>
    </ul>
    <div class="region">
      <svg width="8" height="12" viewBox="0 0 8 12" aria-hidden="true"><path d="M4 0a4 4 0 0 0-4 4c0 3 4 8 4 8s4-5 4-8a4 4 0 0 0-4-4z" fill="#f78f20"/><circle cx="4" cy="4" r="1.5" fill="#fff"/></svg>
      <div>
        <div class="region__label">MY REGION:</div>
        <div class="region__value">NYC <svg width="6" height="4" viewBox="0 0 6 4" aria-hidden="true"><path d="M0.5 0.5 3 3 5.5 0.5" stroke="#7a7a7a" fill="none"/></svg></div>
      </div>
    </div>
    <span class="login">LOGIN</span>
    <span class="join-button">NEW TO BVH?</span>
  </header>

  <section class="hero" role="img" aria-label="Trainer and client exercising outdoors in a green garden">
    <div class="hero__mark"></div>
    <h1 class="hero__name">Brook Vitality &amp; Health</h1>
    <p class="hero__tagline">Care. Strength. Nature.</p>
  </section>

  <section class="intro">
    <div class="intro__col intro__col--training">
      <h2 class="intro__title">OUR TRAINING</h2>
      <p class="intro__text">Personal training for special needs: asthma, diabetes, obesity, rehab and sports performance, for all ages.<br>Small groups, indoors and outdoors, in all weather.</p>
    </div>
    <div class="intro__col intro__col--philosophy">
      <h2 class="intro__title">OUR PHILOSOPHY</h2>
      <p class="intro__text">Real goals, not pipe dreams. Every client is screened and tested, and we work with your allied health professional for the utmost care and lasting results.</p>
    </div>
  </section>

  <div class="benefits-title">
    <span class="benefits-title__dot"></span>
    <h2>TRAIN FOR LIFE.</h2>
  </div>

  <article class="benefit" style="top:622px">
    <div class="benefit__photo photo-care" role="img" aria-label="Trainer guiding a client through a gentle exercise"></div>
    <div class="benefit__body" style="top:37px">
      <h3 class="benefit__heading">SPECIAL NEEDS CARE.</h3>
      <p class="benefit__text">For people with injuries, metabolic or cardio-respiratory conditions, asthma and more. Each program is built around your condition, together with your allied professional, alongside healthy food choices.</p>
    </div>
  </article>

  <article class="benefit" style="top:794px">
    <div class="benefit__photo photo-outdoor" role="img" aria-label="Outdoor training area in a natural garden"></div>
    <div class="benefit__body" style="top:39px">
      <h3 class="benefit__heading">INDOOR &amp; OUTDOOR.</h3>
      <p class="benefit__text">No air-conditioned concrete rooms full of machines. Train in the natural freedom of the elements.<br>A private facility: please ring for an appointment before you visit.</p>
    </div>
  </article>

  <article class="benefit" style="top:972px">
    <div class="benefit__photo photo-pilates" role="img" aria-label="Small Pilates group on mats in a Japanese garden"></div>
    <div class="benefit__body" style="top:39px">
      <h3 class="benefit__heading">PILATES IN THE GARDEN.</h3>
      <p class="benefit__text">Small Pilates group classes in a Japanese garden setting. I work alone, so every group stays small and every client receives a high quality of service.</p>
    </div>
  </article>

  <footer class="site-footer">
    <ul class="site-footer__links">
      <li>HOME PAGE</li>
      <li>MY STORY</li>
      <li>SESSIONS AND PRICING</li>
      <li>COMMUNITY</li>
      <li>CONTACT US</li>
    </ul>
    <span class="site-footer__help">WATCH MY VIDEOS ON CLIPHARBOR</span>
  </footer>
</body>
</html>
```